Hollis Ironworks Business Card

We need a business card design for a new small metal fabrication business in rural NSW, Australia.

The business (Hollis Ironworks) is owner operated by a man with the initials RB - much of the branding comes from this name.

Hollis Ironworks designs, engineers, repairs and manufactures a range of custom, quality metal works including vehicle trays, agricultural machinery impliments, trailers, wood splitters, fire pits, furniture etc.

The brand position focuses on custom work of the highest quality.

Business card design should show quality, attention to detail and stand out among a mass of business cards.

Logos are in the files

The grey color may be changed on the logo if required to stand out more.

There is an image attached of a simple card that is liked because it is clean, clear, simple, masculine and effective. It says 'quality'. As most of the work we do is custom it would be good to have the business card speak to this.

Target Market(s)

Rural and regional based Australians. Primarily adult male 25-60 yrs. Primary production / rural / travelling lifestyle.

Industry/Entity Type

Metal Fabrication

Contact Information for Business Card

The words 'custom quality fabrications' would be great somewhere perhaps on the backside (not on the information side)
Name
title
Phone: 0491 538 274 and (02) 7342 9185
email: info@hollisiw.com.au
www.hollisiw.com.au

address (2 lines)

Requirements
Nice to have
• Background colour should be very navy blue or black.
Should not have
• NO orange and blue combinations.
• Navy is OK

```html
<!DOCTYPE html>
<html lang="en">
<head>
<meta charset="utf-8">
<title>Hollis Ironworks Business Card</title>
<link rel="stylesheet" href="https://fonts.googleapis.com/css2?family=Raleway:wght@300;400;500;700&display=swap">
<style>
  :root {
    --green: #6abf45;
    --green-light: #8fd06f;
    --green-pale: #b5e09e;
    --grey: #96979b;
    --grey-mid: #a9aaad;
    --grey-light: #c4c5c7;
    --paper: #f4f5f7;
    --white: #ffffff;
    --stage: #e9e9ea;
    --ink-soft: #8a8b8f;
  }
  * { box-sizing: border-box; margin: 0; padding: 0; }
  html, body {
    width: 1200px; height: 1000px; overflow: hidden;
    background: var(--stage);
    font-family: "Raleway", sans-serif;
  }
  .card {
    position: absolute; left: 250px;
    width: 700px; height: 389px; overflow: hidden;
    box-shadow: 0 6px 18px rgba(0,0,0,0.18);
  }

  /* Front side */
  .card-front { top: 90px; background: var(--green); }
  .social-strip {
    position: absolute; top: 0; left: 0; right: 0; height: 34px;
    display: flex;
  }
  .social-strip .tile { flex: 1; background: var(--green-light); }
  .social-strip .tile:nth-child(even) { background: #7cc85a; }
  .social-strip .tile:last-child { background: var(--green-pale); }
  .social-handle {
    position: absolute; top: 9px; right: 34px;
    display: flex; align-items: center; gap: 6px;
    color: var(--white); font-size: 12px; font-weight: 500;
  }
  .social-handle .dot { width: 14px; height: 14px; background: var(--white); border-radius: 2px; }
  .brand {
    display: flex; align-items: center; gap: 12px;
    font-weight: 700; letter-spacing: 1px; text-transform: uppercase;
  }
  .brand .mark { width: 42px; height: 42px; }
  .brand-front {
    position: absolute; top: 128px; left: 0; right: 0; justify-content: center;
    color: var(--white); font-size: 30px;
  }
  .brand-front .mark { background: var(--white); }
  .front-base {
    position: absolute; left: 0; right: 0; top: 262px; bottom: 0;
    background: var(--grey); border-top: 6px solid var(--white);
  }
  .tagline {
    position: absolute; top: 22px; left: 0; right: 0; text-align: center;
    color: var(--white); font-size: 19px; font-weight: 500; letter-spacing: 3px;
  }
  .front-base .rule {
    position: absolute; left: 0; right: 0; top: 62px; height: 3px; background: var(--white);
  }

  /* Back side */
  .card-back { top: 521px; background: var(--paper); }
  .brand-back {
    position: absolute; top: 128px; left: 48px;
    color: var(--grey); font-size: 24px;
  }
  .brand-back .mark { background: var(--grey); }
  .holder { position: absolute; top: 56px; left: 420px; }
  .holder-name { color: var(--green); font-size: 32px; font-weight: 300; letter-spacing: -0.5px; }
  .holder-title { color: var(--ink-soft); font-size: 13px; margin: 2px 0 0 26px; }
  .accent-band { position: absolute; left: 385px; right: 0; top: 150px; height: 28px; background: var(--green); }
  .info-block { position: absolute; left: 385px; right: 0; top: 178px; bottom: 0; background: var(--grey); }
  .base-block { position: absolute; left: 0; right: 0; top: 252px; bottom: 0; background: var(--grey); }
  .stripes { position: absolute; left: 314px; top: 196px; display: flex; gap: 4px; }
  .stripes span { width: 20px; height: 56px; }
  .stripes span:nth-child(1) { background: var(--grey); }
  .stripes span:nth-child(2) { background: var(--grey-mid); }
  .stripes span:nth-child(3) { background: var(--grey-light); }
  .contact-list { position: absolute; left: 418px; top: 190px; list-style: none; width: 262px; }
  .contact-list li {
    display: flex; align-items: center; gap: 12px;
    color: var(--white); font-size: 15px; height: 52px;
    border-bottom: 1.5px solid var(--white);
  }
  .contact-list li:last-child { border-bottom: none; }
  .contact-list svg { width: 30px; height: 30px; flex: none; }
</style>
</head>
<body>
  <section class="card card-front">
    <div class="social-strip">
      <span class="tile"></span><span class="tile"></span><span class="tile"></span>
      <span class="tile"></span><span class="tile"></span><span class="tile"></span>
    </div>
    <div class="social-handle"><span class="dot"></span>HollisIronworks</div>
    <div class="brand brand-front"><span class="mark"></span>Hollis Ironworks</div>
    <div class="front-base">
      <p class="tagline">Custom quality fabrications</p>
      <span class="rule"></span>
    </div>
  </section>

  <section class="card card-back">
    <div class="brand brand-back"><span class="mark"></span>Hollis Ironworks</div>
    <div class="holder">
      <p class="holder-name">Rowan Blake</p>
      <p class="holder-title">Director</p>
    </div>
    <div class="accent-band"></div>
    <div class="info-block"></div>
    <div class="base-block"></div>
    <div class="stripes"><span></span><span></span><span></span></div>
    <ul class="contact-list">
      <li>
        <svg viewBox="0 0 30 30" aria-hidden="true">
          <circle cx="15" cy="15" r="13" fill="#fff"/>
          <path d="M10.5 9.5c.8-.8 1.6-.6 2 .1l1.1 1.9c.3.6.1 1.2-.4 1.6l-.7.5c.6 1.6 1.8 2.8 3.4 3.4l.5-.7c.4-.5 1-.7 1.6-.4l1.9 1.1c.7.4.9 1.2.1 2l-1 1c-3.5 1-9.5-5-8.5-8.5z" fill="#96979b"/>
        </svg>
        0491 538 274 / (02) 7342 9185
      </li>
      <li>
        <svg viewBox="0 0 30 30" aria-hidden="true">
          <circle cx="15" cy="15" r="13" fill="#fff"/>
          <rect x="8.5" y="10.5" width="13" height="9" fill="none" stroke="#96979b" stroke-width="1.6"/>
          <path d="M8.5 10.5l6.5 5 6.5-5" fill="none" stroke="#96979b" stroke-width="1.6"/>
        </svg>
        info@hollisiw.com.au
      </li>
      <li>
        <svg viewBox="0 0 30 30" aria-hidden="true">
          <circle cx="15" cy="15" r="13" fill="#fff"/>
          <g fill="none" stroke="#96979b" stroke-width="1.3">
            <circle cx="15" cy="15" r="7"/>
            <ellipse cx="15" cy="15" rx="3" ry="7"/>
            <path d="M8 15h14M9 11.5h12M9 18.5h12"/>
          </g>
        </svg>
        www.hollisiw.com.au
      </li>
    </ul>
  </section>
</body>
</html>
```